Veltana corporate website

Dear graphic designers,
We would like to create a brand new corporate website for our company named "Veltana".
Veltana is a small Swiss premium IT company, with very prestigious clients in the Private Banking industry.
Here would be the values which could be associated to Veltana: trustworthy, serious, modern, high tech, high quality, sobriety, elegant.
Please find attached the Veltana logo in SVG format.
Our new website will have for only purpose to present briefly the company in one page: the team of experts (4 employees), the mission, the expertise and the contact info.
Very short and concise, easy to read.
Like this website for example but even shorter: https://www.dorimel-example.com/

```html
<!DOCTYPE html>
<html lang="en">
<head>
<meta charset="utf-8">
<title>Veltana</title>
<link rel="stylesheet" href="https://fonts.googleapis.com/css2?family=Outfit:wght@300;400;500;600&family=Montserrat:ital,wght@0,400;1,500&display=swap">
<style>
:root{
  --brand:#1458b0;
  --ink:#2f2f2f;
  --muted:#555;
  --soft-blue:#5b7cba;
  --panel:#ececec;
  --card:#f1f1f1;
  --line:#a9a9a9;
  --footer:#e4e4e4;
  --bar:#2b2b2d;
  --white:#fff;
}
*{box-sizing:border-box;margin:0;padding:0}
html,body{width:1200px;height:3999px;overflow:hidden}
body{position:relative;background:var(--white);font-family:"Outfit",sans-serif;color:var(--ink)}
a{text-decoration:none}
.abs{position:absolute}
.brand-name{font-family:"Outfit",sans-serif;font-weight:500;color:var(--brand);letter-spacing:2px;text-transform:uppercase}

/* header */
.site-header{left:0;top:0;width:1200px;height:105px}
.site-header .brand-name{left:75px;top:40px;font-size:30px}
.main-nav{right:75px;top:46px;display:flex;gap:23px;align-items:center;font-size:14px;color:#333}
.main-nav a{color:inherit}
.main-nav .active{color:var(--brand)}

/* hero */
.hero{left:0;top:105px;width:1200px;height:564px;background:linear-gradient(90deg,#f7f7f7 0%,#eeeeee 35%,#c9c3bd 60%,#8f8f95 100%)}
.hero-copy{left:75px;top:125px;width:500px}
.hero-title{font-size:40px;font-weight:400;line-height:54px;color:#333}
.hero-title strong{color:var(--brand);font-weight:600}
.hero-text{margin-top:18px;font-size:14px;line-height:24px;color:var(--muted);white-space:nowrap}
.btn{display:inline-flex;align-items:center;justify-content:center;background:var(--brand);color:var(--white);font-weight:600;border-radius:3px;text-decoration:none}
.hero .btn{position:absolute;left:75px;top:356px;width:155px;height:56px;font-size:21px}

/* team */
.team{left:0;top:782px;width:1200px;height:690px;background:var(--panel)}
.section-title{width:1200px;left:0;text-align:center;font-size:38px;font-weight:400;color:#333}
.section-title strong{color:var(--brand);font-weight:600}
.team .section-title{top:65px}
.team-intro{left:0;width:1200px;top:137px;text-align:center;font-size:14px;line-height:19px;color:#333}
.member{top:258px;width:248px;height:324px;background:var(--white);text-align:center}
.member.is-selected{background:#b9b9b9}
.portrait{position:absolute;left:45px;top:37px;width:158px;height:158px;border-radius:50%}
.member-name{position:absolute;left:0;width:100%;top:236px;font-family:"Montserrat",sans-serif;font-style:italic;font-weight:500;font-size:15px;color:#222}
.member-role{position:absolute;left:0;width:100%;top:270px;font-family:"Montserrat",sans-serif;font-size:13px;color:#555}

/* mission */
.mission-photo{left:75px;top:1569px;width:531px;height:432px;background:linear-gradient(135deg,#8a8d92 0%,#c8bfb1 45%,#6b6660 100%)}
.mission-copy{left:678px;top:1578px;width:480px}
.mission-copy h2{font-size:38px;font-weight:400;color:#333}
.mission-copy h2 strong{color:var(--brand);font-weight:600}
.mission-copy p{font-size:14px;line-height:24px;color:var(--soft-blue);white-space:nowrap}
.mission-copy .lead{margin-top:22px}
.mission-copy h3{font-size:22px;font-weight:400;color:var(--brand);margin-top:50px}
.mission-copy h3+p{margin-top:8px}
.mission-copy h3.tight{margin-top:26px}

/* expertise */
.expertise-title{top:2085px;color:var(--brand);font-weight:600}
.expertise-intro{left:0;width:1200px;top:2158px;text-align:center;font-size:14px;line-height:24px;color:var(--soft-blue)}
.service{top:2282px;width:325px;height:365px;background:var(--card);text-align:center}
.service svg{position:absolute;left:130px;top:40px}
.service h3{position:absolute;left:0;width:100%;top:132px;font-size:22px;font-weight:400;color:var(--brand)}
.service p{position:absolute;left:0;width:100%;top:188px;font-size:14px;line-height:24px;color:var(--soft-blue);white-space:nowrap}
.service a{position:absolute;left:0;width:100%;top:316px;font-size:14px;color:var(--brand)}

/* contact */
.contact-title{top:2745px;color:var(--brand);font-weight:600}
.world-map{background:radial-gradient(ellipse at center,#dcdcdc 0%,#efefef 55%,#fff 80%)}
.map-left{left:0;top:2850px;width:362px;height:615px}
.map-right{left:839px;top:2870px;width:361px;height:555px}
.contact-form{left:362px;top:2832px;width:477px;height:593px;background:var(--white);border:1px solid #e6e6e6}
.form-head{height:71px;background:var(--panel);padding:26px 0 0 24px;font-size:13px;color:#222}
.field-label{position:absolute;left:24px;font-size:13px;color:#333}
.field-label span{color:var(--brand);margin-left:4px}
.field{position:absolute;left:24px;width:422px;height:38px;border:1px solid var(--line);background:var(--white)}
.contact-form .btn{position:absolute;left:162px;top:490px;width:170px;height:62px;font-size:24px}

/* footer */
.site-footer{left:0;top:3553px;width:1200px;height:380px;background:var(--footer)}
.site-footer .brand-name{left:75px;top:48px;font-size:34px}
.footer-about{left:75px;top:126px;width:340px;font-size:17px;line-height:26px;color:#333}
.footer-col{top:52px;font-size:17px;color:#333}
.footer-col h4{font-size:21px;font-weight:400;margin-bottom:14px}
.footer-col li{list-style:none;line-height:26px}
.social{position:absolute;top:156px;width:45px;height:45px;border-radius:50%;background:var(--brand)}
.copyright{left:0;top:3933px;width:1200px;height:66px;background:var(--bar);color:#8a8a8a;font-size:16px;text-align:center;line-height:66px}
</style>
</head>
<body>

<header class="site-header abs">
  <div class="brand-name abs">Veltana</div>
  <nav class="main-nav abs">
    <a class="active" href="#">Home</a><a href="#">About us</a><a href="#">Team</a><a href="#">Services</a><a href="#">Expertise</a><a href="#">Company</a><a href="#">Contact</a>
    <svg width="26" height="26" viewBox="0 0 26 26" fill="none" stroke="#222" stroke-width="2"><circle cx="11" cy="11" r="8"/><path d="M17 17l7 7"/></svg>
  </nav>
</header>

<section class="hero abs" role="img" aria-label="Photo of two smiling colleagues reviewing a document in a bright office">
  <div class="hero-copy abs">
    <h1 class="hero-title"><strong>Lorem Ipsum</strong> is not simply<br>random text</h1>
    <p class="hero-text">Lorem Ipsum available, but the majority have suffered<br>alteration in some form, by injected humour, or randomised words<br>which don't look even slightly believable.</p>
  </div>
  <a class="btn" href="#">About us</a>
</section>

<section class="team abs">
  <h2 class="section-title abs">Our <strong>Team</strong></h2>
  <p class="team-intro abs">Lorem ipsum dolor sit amet, consectetur adipiscing elit,<br>sed do eiusmod tempor incididunt ut labore et dolore magna<br>aliqua. Ut enim ad minim veniam,</p>
  <div class="member abs" style="left:75px"><div class="portrait" role="img" aria-label="Portrait of Leo Brandt" style="background:linear-gradient(#9fd3d8,#2b2f36)"></div><div class="member-name">Leo Brandt</div><div class="member-role">Real Estate Brokered</div></div>
  <div class="member abs is-selected" style="left:344px"><div class="portrait" role="img" aria-label="Portrait of Mira" style="background:linear-gradient(#7c6f62,#1e1e22)"></div><div class="member-name">Mira</div><div class="member-role">Real Estate Brokered</div></div>
  <div class="member abs" style="left:612px"><div class="portrait" role="img" aria-label="Portrait of Ravi" style="background:linear-gradient(#d8d8d8,#2a3443)"></div><div class="member-name">Ravi</div><div class="member-role">Real Estate Brokered</div></div>
  <div class="member abs" style="left:878px"><div class="portrait" role="img" aria-label="Portrait of Lina" style="background:linear-gradient(#8a7d72,#2a2a2e)"></div><div class="member-name">Lina</div><div class="member-role">Real Estate Brokered</div></div>
</section>

<div class="mission-photo abs" role="img" aria-label="Photo of two colleagues working together at laptops"></div>
<div class="mission-copy abs">
  <h2>Our <strong>Mission</strong></h2>
  <p class="lead">Lorem Ipsum available, but the majority have suffered<br>alteration in some form, by injected humour, or randomised words<br>which don't look even slightly believable.</p>
  <h3>Product Designs</h3>
  <p>Skilled professionals are always ready to provide<br>reliable services to our clients!</p>
  <h3 class="tight">Data</h3>
  <p>Skilled professionals are always ready to provide<br>reliable services to our clients!</p>
</div>

<h2 class="section-title expertise-title abs">Expertise</h2>
<p class="expertise-intro abs">Lorem Ipsum available, but the majority have suffered<br>alteration in some form, by injected humour, or randomised words<br>which don't look even slightly believable.</p>

<article class="service abs" style="left:75px">
  <svg width="64" height="64" viewBox="0 0 64 64" fill="none" stroke="#1458b0" stroke-width="2"><circle cx="32" cy="36" r="10"/><path d="M32 20v6M32 46v6M16 36h6M42 36h6M21 25l4 4M43 25l-4 4M21 47l4-4M43 47l-4-4"/><path d="M24 12a11 11 0 0 1 16 0M27 15a6 6 0 0 1 10 0"/></svg>
  <h3>IT Consulting</h3>
  <p>Lorem Ipsum available, but the majority<br>have suffered alteration in some form, by<br>injected humour, or randomised words<br>which don't look even slightly believable.</p>
  <a href="#">Read More</a>
</article>
<article class="service abs" style="left:437px">
  <svg width="64" height="64" viewBox="0 0 64 64" fill="none" stroke="#1458b0" stroke-width="2"><circle cx="38" cy="24" r="7"/><circle cx="38" cy="24" r="14" stroke-dasharray="6 4"/><circle cx="22" cy="42" r="5"/><circle cx="22" cy="42" r="11" stroke-dasharray="5 3"/></svg>
  <h3>IT Consulting</h3>
  <p>Lorem Ipsum available, but the majority<br>have suffered alteration in some form, by<br>injected humour, or randomised words<br>which don't look even slightly believable.</p>
  <a href="#">Read More</a>
</article>
<article class="service abs" style="left:800px">
  <svg width="64" height="64" viewBox="0 0 64 64" fill="none" stroke="#1458b0" stroke-width="2"><path d="M20 8a8 8 0 0 1 8 8c0 6-8 14-8 14s-8-8-8-14a8 8 0 0 1 8-8z"/><circle cx="20" cy="16" r="3"/><path d="M20 34c0 8 10 6 16 8s8 6 2 10"/><ellipse cx="38" cy="48" rx="7" ry="3"/></svg>
  <h3>IT Consulting</h3>
  <p>Lorem Ipsum available, but the majority<br>have suffered alteration in some form, by<br>injected humour, or randomised words<br>which don't look even slightly believable.</p>
  <a href="#">Read More</a>
</article>

<h2 class="section-title contact-title abs">Contact us</h2>
<div class="world-map map-left abs" role="img" aria-label="Dotted world map, the Americas"></div>
<div class="world-map map-right abs" role="img" aria-label="Dotted world map, Europe, Asia and Australia"></div>
<form class="contact-form abs">
  <div class="form-head">Please fill this form in a decent manner</div>
  <label class="field-label" style="top:108px">Full Name<span>*</span></label>
  <div class="field" style="top:141px"></div>
  <label class="field-label" style="top:208px">Email<span>*</span></label>
  <div class="field" style="top:241px"></div>
  <label class="field-label" style="top:308px">Masage<span>*</span></label>
  <div class="field" style="top:341px;height:93px"></div>
  <span class="btn">Submit</span>
</form>

<footer class="site-footer abs">
  <div class="brand-name abs">Veltana</div>
  <p class="footer-about abs">Lorem Ipsum is simply dummy text of the printing and typesetting industry. Lorem Ipsum has been the industry's standard dummy text ever since the 1500s,</p>
  <div class="footer-col abs" style="left:507px"><h4>About us</h4><ul><li>Home</li><li>about</li><li>Services</li><li>Contact</li><li>Products</li></ul></div>
  <div class="footer-col abs" style="left:700px"><h4>Company</h4><ul><li>Events</li><li>Careers</li><li>Terms</li></ul></div>
  <div class="footer-col abs" style="left:912px"><h4>Blog</h4><ul><li>Privacy Policy</li></ul></div>
  <span class="social" style="left:916px" aria-label="Social profile 1"></span>
  <span class="social" style="left:968px" aria-label="Social profile 2"></span>
  <span class="social" style="left:1021px" aria-label="Social profile 3"></span>
  <span class="social" style="left:1074px" aria-label="Social profile 4"></span>
</footer>
<div class="copyright abs">Copyright 2023 &nbsp;NORVIQ. &nbsp;All Right Reserved</div>

</body>
</html>
```